Large multi-office optometry business opening a Dry Eye Spa and needs sign.

Business name/sign info: Brenwick Dry Eye Institute, (555) 362-4817
Backlit pole sign at office entrance on a very busy street
Sign dimensions: 53" tall x 136.5" wide
State of the art Dry Eye Spa for treatment of all forms of dry eye and ocular surface disease. Also, have aesthetics treatments (IPL, Low Level Light Treatment, etc.)

Target Market(s)

People who are suffering from: dryness, burning, foreign body sensation, itching, fluctuating vision, tired eyes, etc.

Industry/Entity Type

Optometry and aesthetics

Colors
0054AA
0677BA
7BADD7
CADEEF
E8F1F8

Requirements
Must have
• Business name, phone number, subliminal message of relief in a glance or short look.
Nice to have
• Cool, relief, soothing sense.
Should not have
• Too much information or too busy.

```html
<!DOCTYPE html>
<html lang="en">
<head>
<meta charset="utf-8">
<title>Brenwick Dry Eye Institute – Sign</title>
<link rel="stylesheet" href="https://fonts.googleapis.com/css2?family=Kanit:wght@600;700&family=Roboto:wght@500&display=swap">
<style>
  :root {
    --brand-blue: #0054AA;
    --brand-red: #EE1C1C;
    --sky: #7BADD7;
    --mist: #CADEEF;
    --ice: #E8F1F8;
    --white: #FFFFFF;
    --backdrop: #E9EDF2;
  }
  html, body {
    margin: 0;
    padding: 0;
    width: 1109px;
    height: 1200px;
    overflow: hidden;
    background: var(--backdrop);
  }
  .canvas {
    position: relative;
    width: 1109px;
    height: 1200px;
  }
  .sign {
    position: absolute;
    left: 0;
    top: 383px;
    width: 1109px;
    height: 433px;
    background: var(--white);
    box-shadow: 0 6px 24px rgba(0, 40, 90, 0.12);
  }
  .sign svg { display: block; }
  .headline {
    font-family: "Kanit", "Arial Black", sans-serif;
    font-weight: 700;
  }
  .headline--place { fill: var(--brand-blue); }
  .headline--service { fill: var(--brand-red); }
  .tagline-pill { fill: var(--brand-blue); }
  .tagline {
    font-family: "Roboto", Arial, sans-serif;
    font-weight: 500;
    fill: var(--white);
  }
  .relief-mark { fill: var(--sky); opacity: 0.75; }
  .base-band { fill: var(--brand-blue); }
  .base-edge { fill: var(--brand-red); }
  .phone {
    font-family: "Kanit", "Arial Black", sans-serif;
    font-weight: 600;
    fill: var(--white);
  }
</style>
</head>
<body>
<main class="canvas">
  <section class="sign" aria-label="Brenwick Dry Eye Institute sign">
    <svg width="1109" height="433" viewBox="0 0 1109 433" xmlns="http://www.w3.org/2000/svg">
      <text class="headline headline--place" x="554.5" y="96" font-size="92" text-anchor="middle" textLength="540" lengthAdjust="spacingAndGlyphs">BRENWICK</text>
      <text class="headline headline--service" x="559" y="186" font-size="98" text-anchor="middle" textLength="957" lengthAdjust="spacingAndGlyphs">DRY EYE INSTITUTE</text>

      <rect class="tagline-pill" x="267" y="213" width="585" height="66" rx="33"/>
      <text class="tagline" x="568" y="258" font-size="33" text-anchor="middle" textLength="480" lengthAdjust="spacingAndGlyphs">State-of-the-art Dry Eye Spa</text>

      <circle class="relief-mark" cx="125" cy="287" r="64" role="img" aria-label="Water drop with soft rays emblem"/>
      <circle class="relief-mark" cx="978" cy="287" r="64" role="img" aria-label="Water drop with soft rays emblem"/>

      <path class="base-edge" d="M0,412 Q554.5,200 1109,412 L1109,433 L0,433 Z"/>
      <path class="base-band" d="M0,422 Q554.5,212 1109,422 L1109,433 L0,433 Z"/>

      <text class="phone" x="554.5" y="410" font-size="70" text-anchor="middle" textLength="495" lengthAdjust="spacingAndGlyphs">555 362 4817</text>
    </svg>
  </section>
</main>
</body>
</html>
```